Can design for new all natural low calorie spiked lemonade

We need a clean but catchy can design for a new spiked lemonade that will be all natural, gluten free and low in calories. Open to any creative ideas ranging from designs such as using a lemonade stand to simple designs such as the example pictures that are uploaded. Looking for a can that just pops out right away on the shelf but also believe less is more as far as simplicity. The beverage is called Brightwell Spiked Lemonade, that features 3 flavors. Traditional Lemonade, Peach Lemonade and lastly Strawberry Lemonade.

Target Market(s)

21-55 years of age. 75% female, 25% male.

Colors

Designer to choose colors to be used in the design.

Requirements
Must have
• The brand name is Brightwell and it is a spiked lemonade so that should be catchy so the consumer knows what it is on first glance. Must say gluten free, all natural, and 150 calories on the front of the can. Would like some type of image on the front middle of the can. There are 3 flavors so the can should blend well with each fruit but not be different cans

```html
<!DOCTYPE html>
<html lang="en">
<head>
<meta charset="utf-8">
<title>Brightwell Spiked Lemonade – Can Labels</title>
<link href="https://fonts.googleapis.com/css2?family=Federo&family=Fjalla+One&family=Yanone+Kaffeesatz:wght@300;500&family=Cormorant+Garamond:wght@500&display=swap" rel="stylesheet">
<style>
  :root {
    --page: #ffffff;
    --label-cream: #eeecd6;
    --ink: #161a14;
    --lemon-green: #3f8f36;
    --berry-red: #d8262c;
    --lemon-a: #f6dc3a;
    --lemon-b: #e9b81c;
    --berry-a: #e8333c;
    --berry-b: #4f9a3a;
    --peach-a: #f0a22c;
    --peach-b: #d8413a;
  }
  * { margin: 0; padding: 0; box-sizing: border-box; }
  html, body {
    width: 1200px; height: 1200px; overflow: hidden;
    background: var(--page);
  }
  .lineup {
    position: absolute; inset: 0;
    display: flex; justify-content: center; align-items: center;
    gap: 70px;
  }
  .can-label {
    position: relative;
    width: 300px; height: 620px;
    background: var(--label-cream);
    border-radius: 6px;
    text-align: center;
    overflow: hidden;
    --accent: var(--berry-red);
  }
  .can-label--lemon { --accent: var(--lemon-green); }
  .brand {
    position: absolute; top: 84px; left: 16px; right: 16px;
    font-family: "Federo", serif;
    font-weight: 400;
    font-size: 39px; letter-spacing: 0;
    line-height: 1;
    white-space: nowrap;
    color: var(--accent);
  }
  .fruit-art {
    position: absolute; top: 170px; left: 30px;
    width: 240px; height: 210px;
    border-radius: 50%;
  }
  .can-label--lemon .fruit-art { background: radial-gradient(circle at 45% 50%, var(--lemon-a), var(--lemon-b) 70%, transparent 72%); }
  .can-label--strawberry .fruit-art { background: radial-gradient(circle at 50% 55%, var(--berry-a), #b81e28 55%, var(--berry-b) 70%, transparent 72%); }
  .can-label--peach .fruit-art { background: radial-gradient(circle at 50% 50%, var(--peach-a), var(--peach-b) 70%, transparent 72%); }
  .flavor {
    position: absolute; top: 408px; left: 0; right: 0;
    font-family: "Cormorant Garamond", serif;
    font-size: 22px; letter-spacing: 5px;
    line-height: 1.2;
    color: var(--accent);
  }
  .product {
    position: absolute; top: 436px; left: 0; right: 0;
    font-family: "Fjalla One", sans-serif;
    font-size: 36px; letter-spacing: -0.5px;
    line-height: 1.2;
    white-space: nowrap;
    color: var(--ink);
  }
  .claims {
    position: absolute; top: 490px; left: 12px; right: 12px;
    display: flex; justify-content: space-between;
    font-family: "Yanone Kaffeesatz", sans-serif; font-weight: 300;
    font-size: 20px; line-height: 1.2;
    color: var(--accent);
  }
  .calories {
    position: absolute; top: 505px; left: 0; right: 0;
    font-family: "Fjalla One", sans-serif;
    color: var(--accent); line-height: 1;
  }
  .calories__number { display: block; font-size: 48px; }
  .calories__unit { display: block; font-size: 24px; margin-top: 6px; }
</style>
</head>
<body>
  <main class="lineup">
    <section class="can-label can-label--lemon">
      <h2 class="brand">BRIGHTWELL</h2>
      <div class="fruit-art" role="img" aria-label="Photograph of fresh lemons with leaves and a cut lemon half"></div>
      <p class="product">SPIKED LEMONADE</p>
      <p class="claims"><span>ALL NATURAL</span><span>GLUTEN FREE</span></p>
      <p class="calories"><span class="calories__number">150</span><span class="calories__unit">CALORIES</span></p>
    </section>
    <section class="can-label can-label--strawberry">
      <h2 class="brand">BRIGHTWELL</h2>
      <div class="fruit-art" role="img" aria-label="Photograph of ripe strawberries with green leaves and a halved berry"></div>
      <p class="flavor">STRAWBERRY</p>
      <p class="product">SPIKED LEMONADE</p>
      <p class="claims"><span>ALL NATURAL</span><span>GLUTEN FREE</span></p>
      <p class="calories"><span class="calories__number">150</span><span class="calories__unit">CALORIES</span></p>
    </section>
    <section class="can-label can-label--peach">
      <h2 class="brand">BRIGHTWELL</h2>
      <div class="fruit-art" role="img" aria-label="Photograph of whole peaches and a halved peach with pit and leaves"></div>
      <p class="flavor">PEACH</p>
      <p class="product">SPIKED LEMONADE</p>
      <p class="claims"><span>ALL NATURAL</span><span>GLUTEN FREE</span></p>
      <p class="calories"><span class="calories__number">150</span><span class="calories__unit">CALORIES</span></p>
    </section>
  </main>
</body>
</html>
```